Business Thank You Cards

I have a thank you card design with a simple chair and my name below it (attached) that I like and that I've used for a while. I started a new company and I'd like to have a similar business thank-your card, but with my company logo (already created) on the back of the chair and the company name "halden brook" where my name is on the attachment, and my contact info on the back of the folding card. Contact info:
halden brook
5184 Mercer Avenue, Suite 270 | Alderton, CA 95742
p. 916.382.4907 | f. 916.259.8063 | ned@haldenbrooklaw.example

```html
<!DOCTYPE html>
<html lang="en">
<head>
<meta charset="utf-8">
<title>Halden Brook — Thank You Card Variations</title>
<link href="https://fonts.googleapis.com/css2?family=Courier+Prime:wght@700&family=Montserrat:wght@600;700;800&display=swap" rel="stylesheet">
<style>
  :root {
    --page: #f4f4f4;
    --blue: #2d5a9c;
    --orange: #fdaa3b;
    --white: #ffffff;
    --ink: #111111;
    --fold-line: rgba(255,255,255,0.28);
    --fold-line-light: rgba(0,0,0,0.12);
  }
  * { box-sizing: border-box; margin: 0; padding: 0; }
  html, body { width: 1200px; height: 1145px; overflow: hidden; }
  body { background: var(--page); position: relative; font-family: "Montserrat", sans-serif; }

  .card { position: absolute; width: 358px; height: 251px; overflow: hidden; }
  .card--blue { background: var(--blue); }
  .card--orange { background: var(--orange); }
  .card--white { background: var(--white); box-shadow: 0 0 0 1px #e6e6e6; }
  .card--raised { box-shadow: 2px 5px 10px rgba(0,0,0,0.35); }
  .card--white.card--raised { box-shadow: 1px 4px 9px rgba(0,0,0,0.25); }

  .fold { position: absolute; inset: 0; width: 100%; height: 100%; }
  .fold line { stroke: var(--fold-line); stroke-width: 1; }
  .card--white .fold line { stroke: var(--fold-line-light); stroke-dasharray: 4 3; }

  .chair-art { position: absolute; left: 50%; top: 48px; width: 112px; height: 132px; transform: translateX(-50%); border-radius: 10px; }
  .chair-art--orange { background: linear-gradient(180deg, rgba(253,170,59,0.55), rgba(253,170,59,0.25)); }
  .chair-art--blue { background: linear-gradient(180deg, rgba(45,90,156,0.5), rgba(45,90,156,0.22)); }

  .card-name { position: absolute; left: 0; right: 0; top: 194px; text-align: center; font-family: "Courier Prime", monospace; font-weight: 700; font-size: 15px; line-height: 18px; color: var(--white); letter-spacing: 0.3px; }

  .wordmark { position: absolute; left: 0; right: 0; top: 196px; display: flex; justify-content: center; align-items: center; gap: 5px; font-weight: 700; font-size: 15px; line-height: 1; }
  .wordmark--white { color: var(--white); }
  .wordmark--blue { color: var(--blue); }
  .wordmark-dot { width: 13px; height: 13px; border-radius: 50%; }
  .wordmark--white .wordmark-dot { background: var(--white); }
  .wordmark--blue .wordmark-dot { background: var(--orange); }
  .wordmark--back { top: 172px; }
  .card--white .wordmark--front { top: 200px; }

  .contact { position: absolute; left: 0; right: 0; top: 202px; text-align: center; font-weight: 700; font-size: 6.6px; line-height: 12px; color: var(--white); white-space: nowrap; }
  .card--white .contact { color: var(--ink); }

  .note { position: absolute; left: 800px; width: 310px; top: 892px; text-align: center; font-weight: 700; font-size: 18px; line-height: 28px; letter-spacing: 1px; color: var(--ink); text-transform: uppercase; }
</style>
</head>
<body>

<!-- Row 1: blue fronts -->
<div class="card card--blue" style="left:30px;top:27px">
  <svg class="fold" viewBox="0 0 358 251" preserveAspectRatio="none"><line x1="0" y1="0" x2="358" y2="251"/><line x1="358" y1="0" x2="0" y2="251"/></svg>
  <div class="chair-art chair-art--orange" role="img" aria-label="Sketched orange office chair with the company mark on its back"></div>
  <p class="card-name">Halden Brook</p>
</div>
<div class="card card--blue" style="left:407px;top:27px">
  <svg class="fold" viewBox="0 0 358 251" preserveAspectRatio="none"><line x1="0" y1="0" x2="358" y2="251"/><line x1="358" y1="0" x2="0" y2="251"/></svg>
  <div class="chair-art chair-art--orange" role="img" aria-label="Sketched orange office chair"></div>
  <p class="card-name">Halden Brook</p>
</div>
<div class="card card--blue" style="left:785px;top:27px">
  <svg class="fold" viewBox="0 0 358 251" preserveAspectRatio="none"><line x1="0" y1="0" x2="358" y2="251"/><line x1="358" y1="0" x2="0" y2="251"/></svg>
  <div class="chair-art chair-art--orange" role="img" aria-label="Sketched orange office chair"></div>
  <div class="wordmark wordmark--white wordmark--front"><span>halden brook</span><span class="wordmark-dot"></span></div>
</div>

<!-- Row 2: orange fronts -->
<div class="card card--orange" style="left:26px;top:300px">
  <svg class="fold" viewBox="0 0 358 251" preserveAspectRatio="none"><line x1="0" y1="0" x2="358" y2="251"/><line x1="358" y1="0" x2="0" y2="251"/></svg>
  <div class="chair-art chair-art--blue" role="img" aria-label="Sketched blue office chair with the company mark on its back"></div>
  <p class="card-name">Halden Brook</p>
</div>
<div class="card card--orange" style="left:403px;top:300px">
  <svg class="fold" viewBox="0 0 358 251" preserveAspectRatio="none"><line x1="0" y1="0" x2="358" y2="251"/><line x1="358" y1="0" x2="0" y2="251"/></svg>
  <div class="chair-art chair-art--blue" role="img" aria-label="Sketched blue office chair"></div>
  <p class="card-name">Halden Brook</p>
</div>
<div class="card card--orange" style="left:781px;top:300px">
  <svg class="fold" viewBox="0 0 358 251" preserveAspectRatio="none"><line x1="0" y1="0" x2="358" y2="251"/><line x1="358" y1="0" x2="0" y2="251"/></svg>
  <div class="chair-art chair-art--blue" role="img" aria-label="Sketched blue office chair"></div>
  <div class="wordmark wordmark--white wordmark--front"><span>halden brook</span><span class="wordmark-dot"></span></div>
</div>

<!-- Row 3: white front, orange and blue backs -->
<div class="card card--white" style="left:26px;top:572px">
  <svg class="fold" viewBox="0 0 358 251" preserveAspectRatio="none"><line x1="0" y1="0" x2="358" y2="251"/><line x1="358" y1="0" x2="0" y2="251"/></svg>
  <div class="chair-art chair-art--blue" role="img" aria-label="Sketched blue office chair" style="height:140px"></div>
  <div class="wordmark wordmark--blue wordmark--front"><span>halden brook</span><span class="wordmark-dot"></span></div>
</div>
<div class="card card--orange card--raised" style="left:404px;top:572px">
  <svg class="fold" viewBox="0 0 358 251" preserveAspectRatio="none"><line x1="0" y1="0" x2="358" y2="251"/><line x1="358" y1="0" x2="0" y2="251"/></svg>
  <div class="wordmark wordmark--white wordmark--back"><span>halden brook</span><span class="wordmark-dot"></span></div>
  <p class="contact">5184 Mercer Avenue, Suite 270 | Alderton, CA 95742<br>p. 916.382.4907 | f. 916.259.8063 | ned@haldenbrooklaw.example</p>
</div>
<div class="card card--blue card--raised" style="left:782px;top:572px">
  <svg class="fold" viewBox="0 0 358 251" preserveAspectRatio="none"><line x1="0" y1="0" x2="358" y2="251"/><line x1="358" y1="0" x2="0" y2="251"/></svg>
  <div class="wordmark wordmark--white wordmark--back"><span>halden brook</span><span class="wordmark-dot"></span></div>
  <p class="contact">5184 Mercer Avenue, Suite 270 | Alderton, CA 95742<br>p. 916.382.4907 | f. 916.259.8063 | ned@haldenbrooklaw.example</p>
</div>

<!-- Row 4: white front and back, note -->
<div class="card card--white" style="left:22px;top:845px">
  <svg class="fold" viewBox="0 0 358 251" preserveAspectRatio="none"><line x1="0" y1="0" x2="358" y2="251"/><line x1="358" y1="0" x2="0" y2="251"/></svg>
  <div class="chair-art chair-art--orange" role="img" aria-label="Sketched orange office chair" style="height:140px"></div>
  <div class="wordmark wordmark--blue wordmark--front"><span>halden brook</span><span class="wordmark-dot"></span></div>
</div>
<div class="card card--white card--raised" style="left:404px;top:845px">
  <svg class="fold" viewBox="0 0 358 251" preserveAspectRatio="none"><line x1="0" y1="0" x2="358" y2="251"/><line x1="358" y1="0" x2="0" y2="251"/></svg>
  <div class="wordmark wordmark--blue wordmark--back"><span>halden brook</span><span class="wordmark-dot"></span></div>
  <p class="contact">5184 Mercer Avenue, Suite 270 | Alderton, CA 95742<br>p. 916.382.4907 | f. 916.259.8063 | ned@haldenbrooklaw.example</p>
</div>

<p class="note">I can send you all<br>this variations<br>so you can have<br>different thank you<br>color cards!</p>

</body>
</html>
```